Marketing , Sales and Distribution Website

This website/this business is specifically to start an international marketing, sales and distribution business - no more than 5 pages - one page design with supporting pages, a strong "call to action" design - lead generation design - Modern - can be easily upgraded.

Target Market(s)

Industrial, engineering, Art, technology, food products, fashion and accessories

Industry/Entity Type

Marketing

Coding

Coded - Design and coding required

Font styles to use
Sans Serif

Requirements
Must have
• user friendly. Fast upload time - space for content. Most have strategic "call to action" lead generation opportunities - space for video, links to social media. room for articles, blogs and upcoming tradeshows - modern interactive website - easy to upgrade in the future. Lastly a link or Tab to a one page site dedicated to mobile marketing subscriptions
Nice to have
• Client login area - backend CRM integration - Hubspot
• I am open to suggestions to make this site attractive for companies who import/export goods - or generate leads of companies who wish to import/export their products to the USA - a lot of this information is in the attachment.

```html
<!DOCTYPE html>
<html lang="en">
<head>
<meta charset="utf-8">
<title>Corvane Marketing</title>
<link rel="stylesheet" href="https://fonts.googleapis.com/css2?family=Roboto:wght@300;400;500;700&display=swap">
<style>
:root{
  --navy:#232b66;
  --navy-deep:#1e2658;
  --sky:#8ba5d8;
  --sky-soft:#9fb5e0;
  --ink:#3a3a3a;
  --muted:#666a73;
  --white:#ffffff;
  --rule:#e4e6ec;
}
*{box-sizing:border-box;margin:0;padding:0}
html,body{width:1200px;height:3340px;overflow:hidden}
body{position:relative;font-family:"Roboto",Arial,sans-serif;color:var(--ink);background:var(--white)}
.abs{position:absolute}

/* header */
.site-header{position:absolute;left:0;top:0;width:1200px;height:118px;background:var(--white);z-index:5}
.brand{position:absolute;left:100px;top:40px;display:flex;align-items:center;gap:12px;z-index:6}
.brand-mark{width:26px;height:26px;background:var(--navy)}
.brand-name{color:var(--navy);font-weight:700;font-size:30px;letter-spacing:1px;line-height:1}
.main-nav{position:absolute;top:50px;right:98px;display:flex;align-items:center;font-size:14px;color:var(--navy)}
.main-nav a{color:var(--navy);text-decoration:none;margin-left:42px;text-transform:uppercase;letter-spacing:.3px}
.main-nav a.is-active{font-weight:700;border-bottom:2px solid var(--navy);padding-bottom:6px}
.main-nav a.ebook{text-transform:none;border:1.5px solid var(--navy);padding:5px 16px}

/* hero */
.hero{position:absolute;left:0;top:118px;width:1200px;height:562px;background:linear-gradient(180deg,#3b3d43 0%,#2a2c31 45%,#4a4245 100%)}
.hero-copy{position:absolute;left:0;top:150px;width:1200px;text-align:center;color:var(--white)}
.hero-title{font-size:42px;font-weight:700;letter-spacing:.5px}
.hero-sub{font-size:23px;font-weight:400;margin-top:14px}
.btn-hero{display:inline-block;margin-top:40px;background:var(--sky);color:var(--white);font-size:19px;padding:12px 30px;letter-spacing:.3px}
.slider-dots{position:absolute;top:472px;left:573px;display:flex;gap:6px}
.slider-dots span{width:14px;height:14px;border-radius:50%;border:2px solid var(--white)}
.slider-dots span.on{background:var(--white)}
.hero-curve{position:absolute;left:0;top:600px;width:1200px;height:82px}

/* section titles */
.section-title{position:absolute;left:0;width:1200px;text-align:center;font-weight:300;font-size:44px;color:var(--navy-deep)}
.section-title .accent{color:var(--navy);font-weight:300}

/* welcome */
.welcome-text{position:absolute;left:180px;top:770px;width:840px;text-align:center;font-size:16px;line-height:28px;color:var(--muted)}
.welcome-rule{position:absolute;left:340px;top:857px;width:520px;height:1px;background:var(--rule)}
.service{position:absolute;top:900px;width:300px;text-align:center}
.service-icon{width:148px;height:148px;border-radius:50%;background:var(--navy);margin:0 auto;display:flex;align-items:center;justify-content:center}
.service-name{font-size:24px;font-weight:400;color:#222;margin-top:22px;letter-spacing:.5px}
.service-text{font-size:16px;line-height:25px;color:var(--muted);margin-top:8px}
.btn-outline{display:inline-block;border:2px solid var(--navy);color:var(--navy);font-size:17px;font-weight:500;padding:10px 24px;margin-top:26px;letter-spacing:.3px}

/* about */
.about{position:absolute;left:0;top:1291px;width:1200px;height:530px;background:linear-gradient(135deg,#2b3578 0%,#3a4790 50%,#27306e 100%);clip-path:polygon(0 0,100% 56px,100% 466px,0 530px)}
.about-title{position:absolute;left:0;top:118px;width:1200px;text-align:center;font-size:46px;font-weight:400;color:var(--white)}
.about-text{position:absolute;left:170px;width:860px;text-align:center;color:var(--white);font-size:17px;line-height:29px}
.btn-ghost{position:absolute;left:452px;top:363px;width:296px;height:51px;border:2px solid rgba(255,255,255,.75);color:var(--white);font-size:15px;font-weight:500;display:flex;align-items:center;justify-content:center;letter-spacing:.3px}

/* video */
.video-copy{position:absolute;left:100px;top:1952px;width:540px;font-size:14px;line-height:26px;color:var(--muted)}
.video-copy p+p{margin-top:26px}
.btn-more{position:absolute;left:100px;top:2180px;width:234px;height:48px;border:2px solid #b9bdc8;color:var(--navy);font-size:16px;font-weight:500;display:flex;align-items:center;justify-content:center;gap:10px}
.video-frame{position:absolute;left:668px;top:1946px;width:436px;height:280px;border:3px solid #d8dadf;background:#fff;padding:12px}
.video-still{position:relative;width:100%;height:228px;background:linear-gradient(135deg,#c9cdd4 0%,#9ea3ab 55%,#6f747c 100%)}
.play{position:absolute;left:168px;top:82px;width:72px;height:72px;border-radius:50%;border:3px solid var(--white)}
.video-bar{height:28px;background:#1b1c20;display:flex;align-items:center;padding:0 12px;gap:12px}
.progress{flex:1;height:5px;background:#555;position:relative}
.progress i{position:absolute;left:0;top:0;width:40%;height:100%;background:var(--sky)}

/* news band */
.news-band{position:absolute;left:0;top:2270px;width:1200px;height:740px;background:var(--sky);clip-path:polygon(0 67px,100% 0,100% 100%,0 100%)}
.col-title{position:absolute;top:2400px;font-size:30px;color:var(--navy-deep);font-weight:400}
.col-rule{position:absolute;top:2460px;width:1px;height:430px;background:rgba(255,255,255,.35)}
.article-photo{position:absolute;left:100px;top:2475px;width:292px;height:168px;border:4px solid var(--white);background:linear-gradient(135deg,#5d5a55 0%,#3f3d3a 60%,#8b8780 100%)}
.article-text{position:absolute;left:100px;top:2660px;width:320px;font-size:13px;line-height:21px;color:var(--white)}
.btn-read{position:absolute;left:100px;top:2800px;width:126px;height:42px;border:2px solid var(--white);color:var(--white);font-size:15px;display:flex;align-items:center;justify-content:center;gap:8px}
.show{position:absolute;left:481px;width:360px}
.show-date{position:absolute;left:0;top:0;width:98px;height:98px;border-radius:50%;border:2px solid rgba(255,255,255,.85);color:var(--white);text-align:center}
.show-day{font-size:44px;font-weight:300;line-height:44px;margin-top:16px}
.show-month{font-size:11px;margin-top:2px}
.show-title{position:absolute;left:116px;top:14px;color:var(--white);font-size:14px;font-weight:500;letter-spacing:.3px}
.show-text{position:absolute;left:116px;top:38px;width:220px;color:var(--white);font-size:12px;line-height:18px}
.blog-photo{position:absolute;left:879px;width:202px;height:108px;border:4px solid var(--white);background:linear-gradient(135deg,#8d95a3 0%,#5d6472 60%,#aab0bb 100%)}
.blog-photo.alt{background:linear-gradient(135deg,#e6e9ee 0%,#b9c4d1 55%,#9bbf8a 100%)}
.blog-title{position:absolute;left:879px;color:var(--navy-deep);font-size:13px;font-weight:500;letter-spacing:.2px}
.blog-text{position:absolute;left:879px;width:230px;color:var(--white);font-size:11.5px;line-height:16px}

/* footer */
.site-footer{position:absolute;left:0;top:2938px;width:1200px;height:402px;background:var(--navy-deep);clip-path:polygon(0 0,100% 56px,100% 100%,0 100%);color:var(--white)}
.foot-col{position:absolute;top:112px}
.foot-head{font-size:14px;font-weight:700;letter-spacing:.4px;margin-bottom:16px}
.foot-list{list-style:none;font-size:12px;line-height:25px;color:#d8dcef}
.foot-text{font-size:12px;line-height:19px;color:#d8dcef;width:250px}
.subscribe-input{margin-top:22px;width:244px;height:40px;background:var(--white);color:#888;font-size:12px;padding:12px}
.subscribe-btn{margin-top:12px;width:92px;height:40px;background:var(--sky);color:var(--white);font-size:12px;display:flex;align-items:center;justify-content:center}
.foot-sep{position:absolute;top:108px;width:1px;height:200px;background:rgba(255,255,255,.12)}
.contact-line{display:flex;align-items:center;gap:10px}
.foot-bottom{position:absolute;left:100px;top:359px;width:1080px;font-size:11px;color:#d8dcef;display:flex;justify-content:space-between;align-items:center}
.social{display:flex;align-items:center;gap:14px}
.social span{width:12px;height:12px;border-radius:50%;background:#d8dcef;display:inline-block}
</style>
</head>
<body>

<header class="site-header">
  <div class="brand"><span class="brand-mark"></span><span class="brand-name">CORVANE</span></div>
  <nav class="main-nav">
    <a class="is-active">Home</a><a>About Us</a><a>Services</a><a>Blog</a><a>News</a><a>Contact</a><a>Login</a><a class="ebook">e-book</a>
  </nav>
</header>

<section class="hero" role="img" aria-label="Photo of a busy trade show hall with exhibition stands seen from above">
  <div class="hero-copy">
    <h1 class="hero-title">CORVANE MARKETING</h1>
    <p class="hero-sub">We are an international marketing, sales and distribution business</p>
    <span class="btn-hero">GET IN TOUCH</span>
  </div>
  <div class="slider-dots"><span></span><span class="on"></span><span class="on"></span></div>
</section>
<svg class="hero-curve" viewBox="0 0 1200 82" preserveAspectRatio="none"><path d="M0 0 Q600 150 1200 0 L1200 82 L0 82Z" fill="#fff"/></svg>

<h2 class="section-title" style="top:706px">Welcome to <span class="accent">Corvane</span></h2>
<p class="welcome-text">Sed do eiusmod tempor incididunt ut labore et dolore magna aliqua. Ut enim ad minim veniam, quis nostrud exercitation ullamco laboris nisi.</p>
<div class="welcome-rule"></div>

<div class="service" style="left:90px">
  <div class="service-icon">
    <svg width="84" height="74" viewBox="0 0 84 74"><g fill="#fff"><rect x="10" y="50" width="10" height="20"/><rect x="25" y="40" width="10" height="30"/><rect x="40" y="30" width="10" height="40"/><rect x="55" y="20" width="10" height="50"/><rect x="4" y="70" width="72" height="3"/></g><path d="M8 40 Q40 30 64 8" stroke="#fff" stroke-width="5" fill="none"/><path d="M56 4 L72 2 L68 18Z" fill="#fff"/></svg>
  </div>
  <h3 class="service-name">MARKETING</h3>
  <p class="service-text">Sed ut perspiciatis unde omnis iste natus error sit voluptatem accusantium.</p>
  <span class="btn-outline">READ MORE</span>
</div>
<div class="service" style="left:449px">
  <div class="service-icon">
    <svg width="90" height="60" viewBox="0 0 90 60"><g fill="#fff"><path d="M0 14 L18 8 L30 36 L12 42Z"/><path d="M90 14 L72 8 L60 36 L78 42Z"/><path d="M22 16 L42 10 L56 14 L70 12 L62 38 L48 52 L36 50 L24 38Z"/></g><path d="M40 18 L52 26" stroke="#232b66" stroke-width="3"/></svg>
  </div>
  <h3 class="service-name">SALES</h3>
  <p class="service-text">Sed ut perspiciatis unde omnis iste natus error sit voluptatem accusantium.</p>
  <span class="btn-outline">READ MORE</span>
</div>
<div class="service" style="left:809px">
  <div class="service-icon">
    <svg width="84" height="70" viewBox="0 0 84 70"><g fill="#fff"><path d="M6 26 L20 26 L56 6 L56 62 L20 44 L6 44Z"/><path d="M20 46 L30 46 L36 66 L26 66Z"/></g><g stroke="#fff" stroke-width="4" fill="none" stroke-linecap="round"><path d="M64 24 Q70 34 64 44"/><path d="M72 16 Q82 34 72 52"/></g></svg>
  </div>
  <h3 class="service-name">DISTRIBUTION</h3>
  <p class="service-text">Sed ut perspiciatis unde omnis iste natus error sit voluptatem accusantium.</p>
  <span class="btn-outline">READ MORE</span>
</div>

<section class="about" role="img" aria-label="Blue tinted photo of business people in a bright office">
  <h2 class="about-title">About Corvane</h2>
  <p class="about-text" style="top:190px">But I must explain to you how all this mistaken idea of denouncing pleasure and praising pain was born and I will give you a complete account of the system.</p>
  <p class="about-text" style="top:268px">At vero eos et accusamus et iusto odio dignissimos ducimus qui blanditiis praesentium voluptatum deleniti atque corrupti quos dolores et quas molestias excepturi sint occaecati cupiditate.</p>
  <span class="btn-ghost">LEAD GENERATION OPPORTUNITIES</span>
</section>

<h2 class="section-title" style="top:1848px">Our Video</h2>
<div class="video-copy">
  <p>Sed ut perspiciatis unde omnis iste natus error sit voluptatem accusantium doloremque laudantium, totam rem aperiam, eaque ipsa quae ab illo inventore veritatis et quasi architecto beatae vitae dicta sunt explicabo.</p>
  <p>Ut enim ad minim veniam, quis nostrud exercitation ullamco laboris nisi ut aliquip ex ea commodo consequat. Duis aute irure dolor in reprehenderit in voluptate velit esse cillum dolore eu fugiat nulla pariatur. Excepteur sint occaecat cupidatat non proident.</p>
</div>
<span class="btn-more">MORE INFORMATION <svg width="8" height="12" viewBox="0 0 8 12"><path d="M1 1 L6 6 L1 11" stroke="#232b66" stroke-width="2" fill="none"/></svg></span>
<div class="video-frame">
  <div class="video-still" role="img" aria-label="Video still of hands reviewing papers with a pen on a desk">
    <span class="play"></span>
    <svg class="abs" style="left:196px;top:104px" width="26" height="30" viewBox="0 0 26 30"><path d="M2 2 L24 15 L2 28Z" fill="none" stroke="#fff" stroke-width="3"/></svg>
  </div>
  <div class="video-bar">
    <svg width="10" height="12" viewBox="0 0 10 12"><path d="M0 0 L10 6 L0 12Z" fill="#fff"/></svg>
    <div class="progress"><i></i></div>
    <svg width="14" height="12" viewBox="0 0 14 12"><path d="M0 4 H3 L7 0 V12 L3 8 H0Z" fill="#fff"/><path d="M9 3 Q12 6 9 9" stroke="#fff" fill="none" stroke-width="1.5"/></svg>
  </div>
</div>

<section class="news-band"></section>
<h2 class="col-title" style="left:100px">Articles</h2>
<h2 class="col-title" style="left:488px">Upcoming Tradeshows</h2>
<h2 class="col-title" style="left:875px">Our Blogs</h2>
<div class="col-rule" style="left:445px"></div>
<div class="col-rule" style="left:838px"></div>

<div class="article-photo" role="img" aria-label="Photo of a laptop and coffee cup on a wooden desk"></div>
<p class="article-text">Praesent a accumsan est. Nam ornare erat sed tortor iaculis posuere. Suspendisse tempus luctus nunc, ut laoreet leo. Nam neque tellus, ornare vitae lobortis id, sagittis vitae arcu. Maecenas a adipiscing nisi. Nullam sed risus sit amet ipsum lobortis condimentum.</p>
<span class="btn-read">Read More <svg width="7" height="11" viewBox="0 0 7 11"><path d="M1 1 L5.5 5.5 L1 10" stroke="#fff" stroke-width="1.8" fill="none"/></svg></span>

<div class="show" style="top:2466px">
  <div class="show-date"><div class="show-day">09</div><div class="show-month">JAN / 2017</div></div>
  <div class="show-title">NOSTRUD EXERCITATION</div>
  <p class="show-text">Suspendisse tempus luctus nunc, ut laoreet leo. Nam neque tellus, ornare vitae lobortis.</p>
</div>
<div class="show" style="top:2602px">
  <div class="show-date"><div class="show-day">04</div><div class="show-month">FEB / 2017</div></div>
  <div class="show-title">UNDE OMNIS ISTE NATUS</div>
  <p class="show-text">Suspendisse tempus luctus nunc, ut laoreet leo. Nam neque tellus, ornare vitae lobortis.</p>
</div>
<div class="show" style="top:2738px">
  <div class="show-date"><div class="show-day">15</div><div class="show-month">JAN / 2017</div></div>
  <div class="show-title">OFFICIA DESERUNT MOLLIT</div>
  <p class="show-text">Suspendisse tempus luctus nunc, ut laoreet leo. Nam neque tellus, ornare vitae lobortis.</p>
</div>

<div class="blog-photo" style="top:2471px" role="img" aria-label="Photo of a team meeting around a conference table"></div>
<div class="blog-title" style="top:2590px">PRAESENT A ACCUMSAN EST</div>
<p class="blog-text" style="top:2610px">At vero eos et accusamus est iusto odio dignissimos ducimus qui blanditiis</p>
<div class="blog-photo alt" style="top:2671px" role="img" aria-label="Photo of printed charts and a pen on a desk"></div>
<div class="blog-title" style="top:2790px">MAURIS FERMENTUM MAGNA</div>
<p class="blog-text" style="top:2810px">Donec sit amet eros. Lorem ipsum dolor sit amet consectetuer adipiscing elit</p>

<footer class="site-footer">
  <div class="foot-col" style="left:100px">
    <div class="foot-head">LINKS</div>
    <ul class="foot-list"><li>Home</li><li>Sales</li><li>Marketing</li><li>Distribution</li><li>Ebook</li><li>Login</li></ul>
  </div>
  <div class="foot-sep" style="left:220px"></div>
  <div class="foot-col" style="left:254px">
    <div class="foot-head">JOIN OUR NEWSLETTER</div>
    <p class="foot-text">Excepteur sint occaecat cupidatat non proident, sunt in culpa qui</p>
    <div class="subscribe-input">Enter Your Email</div>
    <div class="subscribe-btn">SUBSCRIBE</div>
  </div>
  <div class="foot-sep" style="left:550px"></div>
  <div class="foot-col" style="left:590px">
    <div class="foot-head">INFORMATION</div>
    <ul class="foot-list"><li>Terms &amp; Conditions</li><li>Privacy policy</li><li>Disclaimer</li><li>Contact us</li><li>Sitemap</li></ul>
  </div>
  <div class="foot-col" style="left:786px">
    <div class="foot-head">WHY US</div>
    <ul class="foot-list"><li>Customers</li><li>Team</li><li>FAQ</li><li>News</li><li>Others</li></ul>
  </div>
  <div class="foot-sep" style="left:920px"></div>
  <div class="foot-col" style="left:953px">
    <div class="foot-head">CONTACT INFO</div>
    <ul class="foot-list">
      <li style="font-weight:700;color:#fff">Corvane</li>
      <li style="line-height:22px">NO, Street Name,<br>City Name, Country.</li>
      <li class="contact-line"><svg width="12" height="12" viewBox="0 0 12 12"><path d="M2 1 L4.5 1 L5.5 4 L4 5 Q5 7.5 7 8 L8 6.5 L11 7.5 L11 10 Q6 12 2 6 Q0.5 3 2 1Z" fill="#fff"/></svg>+10 (0) 555 014 72</li>
      <li class="contact-line"><svg width="13" height="10" viewBox="0 0 13 10"><rect width="13" height="10" fill="#fff"/><path d="M0 0 L6.5 5.5 L13 0" stroke="#1e2658" fill="none"/></svg>info@corvane-mail.com</li>
    </ul>
  </div>
  <div class="foot-bottom">
    <span>© 2017. Corvane. All rights reserved</span>
    <span class="social">Connect with our social network : <span></span><span></span><span></span><span></span><span></span></span>
  </div>
</footer>

</body>
</html>
```